Create a Magazine Ad for an asbestos law firm

we need an 8 X 13 ad to be on the back of a magazine cover. We have the text Attached and want a similar look and feel to our website : www.harborvale-claims.example. The ad should be targeted to white males 55 years or older who are conservative and worked in industry or industrial plants. The main offer is a free case review and trying to get them to call the telephone number.

Target Market(s)

White collar men who worked in industrial plants. Age 55 years or older.

Industry/Entity Type

Legal

Requirements
Must have
• Pictures of white middle class conservative man or man and woman
Nice to have
• look at www.harborvale-claims.example to an. idea of what we are looking for

```html
<!DOCTYPE html>
<html lang="en">
<head>
<meta charset="utf-8">
<title>Mesothelioma Compensation – Magazine Ad</title>
<link rel="stylesheet" href="https://fonts.googleapis.com/css2?family=Poppins:wght@400;500;600;700&display=swap">
<style>
:root{
  --gold:#8c6428;
  --gold-dark:#5c3f14;
  --navy:#0d2438;
  --ink:#141414;
  --sand:#e3dbd0;
  --sand-deep:#ddd3c6;
  --tan-block:#e2d9cc;
  --white:#ffffff;
}
*{margin:0;padding:0;box-sizing:border-box}
html,body{width:738px;height:1200px;overflow:hidden;background:var(--white)}
body{font-family:'Poppins',sans-serif;color:var(--ink)}
.ad{position:relative;width:738px;height:1200px;overflow:hidden;background:var(--white)}
.decor{position:absolute;inset:0}
.logo-box{position:absolute;left:16px;top:0;width:191px;height:190px;background:var(--gold);
  color:var(--white);font-weight:700;font-size:55px;line-height:57px;letter-spacing:2px;padding:50px 0 0 15px}
.headline{position:absolute;left:15px;top:296px;letter-spacing:1.6px;line-height:35px;white-space:nowrap}
.headline .l1{font-size:31px;font-weight:600;color:var(--gold-dark)}
.headline .l2{font-size:31px;font-weight:700;color:var(--gold)}
.sub{position:absolute;left:15px;top:373px;font-size:20px;font-weight:600;color:var(--navy);letter-spacing:1.6px;line-height:23px;white-space:nowrap}
.sub-rule{position:absolute;left:206px;top:411px;width:110px;height:3px;background:var(--gold)}
.copy{position:absolute;left:15px;font-size:9.4px;font-weight:600;letter-spacing:.5px;line-height:12.3px;white-space:nowrap}
.list{position:absolute;left:15px;list-style:none;font-size:9.6px;font-weight:400;letter-spacing:.7px;line-height:12.3px;white-space:nowrap}
.list li::before{content:"• "}
.lead{position:absolute;left:15px;top:520px;font-size:14px;font-weight:600;letter-spacing:.8px;line-height:16.5px;white-space:nowrap}
.section-title{position:absolute;left:15px;font-size:18.5px;font-weight:500;letter-spacing:1.7px;line-height:22px;color:var(--gold-dark);white-space:nowrap}
.section-title b{font-weight:700;color:var(--gold)}
.cases{position:absolute;top:863px;height:192px;background:linear-gradient(var(--sand),var(--sand-deep))}
.case{position:absolute;left:15px}
.amount{display:block;width:142px;height:26px;border-radius:5px;background:linear-gradient(#8a6226,#5e4014);
  color:var(--white);font-size:17px;font-weight:600;letter-spacing:1.6px;line-height:26px;padding-left:17px}
.label{display:block;margin-top:6px;font-size:13.2px;font-weight:500;letter-spacing:.9px;white-space:nowrap}
.cta{position:absolute;left:15px;top:1093px;font-size:13.6px;font-weight:600;letter-spacing:.9px;line-height:16px;white-space:nowrap}
.cta em{font-style:normal;font-weight:700;color:var(--gold)}
.credit{position:absolute;left:15px;top:1162px;font-size:10px;letter-spacing:.6px}
</style>
</head>
<body>
<div class="ad">
  <svg class="decor" width="738" height="1200" viewBox="0 0 738 1200">
    <defs>
      <linearGradient id="ring" x1="0" y1="0" x2="1" y2="1">
        <stop offset="0" stop-color="#d4d4d6"/><stop offset="1" stop-color="#f4f4f5"/>
      </linearGradient>
      <linearGradient id="photo" x1="0" y1="0" x2="0" y2="1">
        <stop offset="0" stop-color="#e9eef3"/>
        <stop offset=".3" stop-color="#c9d3dc"/>
        <stop offset=".45" stop-color="#7f9dc6"/>
        <stop offset="1" stop-color="#6a88b4"/>
      </linearGradient>
    </defs>
    <rect x="0" y="0" width="30" height="22" fill="var(--tan-block)"/>
    <rect x="265" y="-10" width="52" height="73" rx="6" fill="var(--tan-block)"/>
    <rect x="686" y="632" width="60" height="76" rx="6" fill="var(--tan-block)"/>
    <rect x="0" y="1125" width="383" height="80" fill="var(--tan-block)"/>
    <rect x="320" y="1168" width="430" height="40" rx="6" fill="var(--tan-block)"/>
    <circle cx="762" cy="176" r="466" fill="url(#ring)"/>
    <circle cx="770" cy="172" r="448" fill="url(#photo)" role="img" aria-label="Photo of a smiling older man with a white beard and glasses, in a blue shirt, holding a folder and pen"/>
  </svg>

  <div class="logo-box">LOGO<br>HERE</div>

  <h1 class="headline"><span class="l1">DIAGNOSED WITH</span><br><span class="l2">MESOTHELIOMA,</span></h1>
  <h2 class="sub">YOU COULD BE OWED<br>COMPENSATION</h2>
  <div class="sub-rule"></div>

  <p class="copy" style="top:430px">It's very likely you developed this disease through asbestos<br>exposure. Mesothelioma patients are getting multi-million<br>dollar settlements, decades later, from:</p>
  <ul class="list" style="top:478px">
    <li>Exposure to asbestos products,</li>
    <li>Ex-employers, or</li>
    <li>Talcum baby powder companies.</li>
  </ul>

  <p class="lead">We can help you find out if you<br>qualify for a case in minutes.</p>
  <ul class="list" style="top:565px">
    <li>We'll analyze your situation at no cost</li>
    <li>Determine how much compensation you could be entitled</li>
    <li>too Show you the next steps to get what you're owed</li>
  </ul>

  <h2 class="section-title" style="top:613px"><b>$30 BILLION</b> IS AVAILABLE IN<br>TRUST FOR <b>MESOTHELIOMA</b> PATIENTS</h2>
  <p class="copy" style="top:664px">Tradesmen in many industries were negligently exposed to asbestos materials<br>well into the 1990s. Whether you developed Mesothelioma yourself due to as-<br>bestos exposure or you're the surviving family of a lost loved one you could be<br>entitled to significant compensation.</p>

  <h2 class="section-title" style="top:735px">HOW MUCH MONEY CAN PEOPLE RECEIVE<br>FROM A <b>MESOTHELIOMA CASE?</b></h2>
  <p class="copy" style="top:791px">Depending on where you were exposed and a few other factors, you can get a<br>settlement from 6 to 7 figures. Here are a few examples of Mesothelioma Settle-<br>ments received by our clients. These figures are the total compensation after<br>all attorney fees and expenses are deducted.</p>

  <section class="cases" style="left:0;width:366px">
    <div class="case" style="top:10px"><span class="amount">$6,142,500</span><span class="label">Exposed through heavy duty vehicles</span></div>
    <div class="case" style="top:75px"><span class="amount">$6,033,510</span><span class="label">Exposed through general contracting</span></div>
    <div class="case" style="top:136px"><span class="amount">$5,939,010</span><span class="label">Exposed through boat repair</span></div>
  </section>
  <section class="cases" style="left:372px;width:366px">
    <div class="case" style="left:55px;top:10px"><span class="amount">$3,921,750</span><span class="label">Exposed through navy service</span></div>
    <div class="case" style="left:55px;top:75px"><span class="amount">$3,600,450</span><span class="label">Exposed through navy service</span></div>
    <div class="case" style="left:55px;top:136px"><span class="amount">$2.5 Million</span><span class="label">Exposed from Avo Talcum Baby Powder</span></div>
  </section>

  <p class="cta"><em>FIND OUT IF YOU'RE ELIGIBLE, FOR FREE, IN MINUTES.</em> We'll evaluate<br>your situation and tell you what your case could be worth. <em>GET</em><br><em>YOUR FREE EVALUATION NOW! CALL 1-XXX XXXX (GOOD</em><br><em>NUMBER)</em></p>
  <p class="credit">Marlow &amp; Pryce, LLP, Owen Marlow, Brookfield, OH</p>
</div>
</body>
</html>
```